PITCH PRESENTATION for Feature Film Project

A while ago I had some key art designed for me for a film project called Ember Crane's Oath (I see it's still in the online portfolio for pixelorchard, who did the original work). I'm now taking that project to a series of pitch meetings at a film festival here in Canada and am putting together a powerpoint presentation.
I would want you to use the original design/aesthetic framework across the 14 pages of the presentation. I have provided the text and some image ideas (there's also one video to insert) that you may or may not use, etc. Probably for a large chunk of the pages - perhaps 6 of the ten - you could just clean it up and create a common background theme on which to place the companion text. Obviously, while making it pretty is a priority, it's also a priority for it to be legible to the people whom I'm pitching the project when it is projected onto a large screen.
I've uploaded a draft of the powerpoint text - there could be some minor changes between now and next week. I'll be leaving for the festival on December 3 so, obviously need a final version before that date. I've attached a .jpg of the original artwork along with the powerpoint.

Let me know if you need more details.
Updates

I wasn't able to upload the .psd file of the original poster artwork with layers & fonts but here is a link to download it from my dropbox: https://www.filevaultly.net/s/k3p8tqzr1mw4xa/FA-Ember%20Crane%27s%20Oath%20poster.psd?dl=0 best Derek

Target Market(s)

This is targeted at some Chinese studio executives to whom the project will be pitched. It is for a film that is a martial arts thriller.

Industry/Entity Type

Festival

Requirements
Must have
• The main thing is to use the already-existing material (the poster - incl colour scheme and fonts) as the aesthetic foundation for the presentation. We are, in a sense, trying to strengthen the brand identity of the project with the execs.

```html
<!DOCTYPE html>
<html lang="en">
<head>
<meta charset="utf-8">
<title>Ember Crane's Oath — Pitch Slide</title>
<link rel="stylesheet" href="https://fonts.googleapis.com/css2?family=Cinzel:wght@600;700&family=PT+Sans:wght@400&display=swap">
<style>
  :root {
    --bg-core: #5e1c12;
    --bg-mid: #45120b;
    --bg-edge: #260806;
    --glow: rgba(190, 90, 45, 0.22);
    --glow-soft: rgba(170, 70, 35, 0.14);
    --gold: #e2b646;
    --gold-deep: #c79a3a;
    --caption: #f3ece4;
    --photo-top: #8a8f96;
    --photo-red: #a8463a;
    --photo-blue: #86bccb;
    --photo-low: #9a8256;
    --photo-floor: #cfcac2;
    --thumb-top: #4a140e;
    --thumb-mid: #8a3020;
    --thumb-low: #2a0805;
  }
  html, body {
    margin: 0;
    padding: 0;
    width: 900px;
    height: 1200px;
    overflow: hidden;
    background: var(--bg-edge);
  }
  .slide {
    position: relative;
    width: 900px;
    height: 1200px;
    overflow: hidden;
    background:
      radial-gradient(ellipse 75% 55% at 50% 38%, var(--bg-core) 0%, var(--bg-mid) 55%, var(--bg-edge) 100%);
  }
  .bokeh-texture {
    position: absolute;
    inset: 0;
    background:
      radial-gradient(circle 70px at 90px 1020px, var(--glow) 0%, transparent 100%),
      radial-gradient(circle 55px at 250px 1090px, var(--glow-soft) 0%, transparent 100%),
      radial-gradient(circle 80px at 190px 860px, var(--glow-soft) 0%, transparent 100%),
      radial-gradient(circle 45px at 400px 960px, var(--glow) 0%, transparent 100%),
      radial-gradient(circle 60px at 470px 1130px, var(--glow-soft) 0%, transparent 100%),
      radial-gradient(circle 50px at 560px 880px, var(--glow-soft) 0%, transparent 100%),
      radial-gradient(circle 40px at 60px 780px, var(--glow-soft) 0%, transparent 100%),
      radial-gradient(circle 65px at 330px 800px, var(--glow-soft) 0%, transparent 100%),
      radial-gradient(circle 50px at 40px 1170px, var(--glow) 0%, transparent 100%),
      radial-gradient(circle 45px at 820px 160px, var(--glow-soft) 0%, transparent 100%),
      radial-gradient(circle 45px at 90px 300px, var(--glow-soft) 0%, transparent 100%);
  }
  .slide-title {
    position: absolute;
    top: 20px;
    left: 0;
    width: 100%;
    margin: 0;
    text-align: center;
    font-family: "Cinzel", "Times New Roman", serif;
    font-weight: 700;
    font-size: 46px;
    line-height: 56px;
    letter-spacing: 1px;
    color: var(--gold);
  }
  .still-photo {
    position: absolute;
    left: 249px;
    top: 84px;
    width: 402px;
    height: 570px;
    background:
      radial-gradient(ellipse 22% 55% at 50% 48%, rgba(134, 188, 203, 0.85) 0%, transparent 100%),
      linear-gradient(90deg, rgba(168, 70, 58, 0.55) 0%, transparent 30%, transparent 75%, rgba(120, 110, 80, 0.45) 100%),
      linear-gradient(180deg, var(--photo-top) 0%, var(--photo-blue) 35%, var(--photo-low) 70%, var(--photo-floor) 100%);
  }
  .logline {
    position: absolute;
    left: 30px;
    top: 674px;
    width: 840px;
    margin: 0;
    text-align: center;
    font-family: "PT Sans", Arial, sans-serif;
    font-size: 24px;
    line-height: 34px;
    color: var(--caption);
  }
  .key-art {
    position: absolute;
    left: 650px;
    top: 880px;
    width: 240px;
    height: 240px;
    background: radial-gradient(ellipse 45% 55% at 50% 35%, var(--thumb-mid) 0%, var(--thumb-top) 60%, transparent 100%);
    opacity: 0.9;
  }
  .key-art-title {
    position: absolute;
    right: 22px;
    top: 1118px;
    width: 300px;
    margin: 0;
    text-align: right;
    font-family: "Cinzel", "Times New Roman", serif;
    font-weight: 600;
    font-size: 30px;
    line-height: 36px;
    color: var(--gold-deep);
  }
  .key-art-title span { display: block; }
</style>
</head>
<body>
  <main class="slide">
    <div class="bokeh-texture" role="img" aria-label="Soft blurred ember glows across a dark red backdrop"></div>
    <h1 class="slide-title">Ember Crane's Oath</h1>
    <div class="still-photo" role="img" aria-label="Film still: a young woman in a light blue top and patterned trousers standing in a warehouse, holding weapons"></div>
    <p class="logline">A widow's act of vengeance brings the wrath of both the Triad and the police down upon her and her loved ones.</p>
    <div class="key-art" role="img" aria-label="Small faded version of the film's key art poster"></div>
    <p class="key-art-title"><span>Ember Crane's</span><span>Oath</span></p>
  </main>
</body>
</html>
```